Letterhead and Stationary for Construction Company

Brisk Current needs modern Letterhead, Envelopes and Notepad designs.

Industry/Entity Type

Construction

Colors
f78f20
34a7d8
ffffff

Requirements
Must have
• Modern looking design.

```html
<!DOCTYPE html>
<html lang="en">
<head>
<meta charset="utf-8">
<title>Brisk Current — Stationery Set</title>
<link href="https://fonts.googleapis.com/css2?family=Open+Sans:wght@600&display=swap" rel="stylesheet">
<style>
  :root {
    --backdrop: #a8a8a8;
    --paper: #ffffff;
    --blue-deep: #0a7fc2;
    --blue: #0094dc;
    --orange: #e87a1e;
    --brand-ink: #2c5ea6;
    --rule: #e2e2e2;
  }
  * { margin: 0; padding: 0; box-sizing: border-box; }
  html, body { width: 1200px; height: 842px; overflow: hidden; }
  body { background: var(--backdrop); position: relative; font-family: "Open Sans", Arial, sans-serif; }

  .sheet { position: absolute; background: var(--paper); overflow: hidden; }

  .brand { position: absolute; display: flex; align-items: center; gap: 6px; white-space: nowrap; }
  .brand-dot { border-radius: 50%; background: var(--orange); flex: none; }
  .brand-name { color: var(--brand-ink); font-weight: 600; letter-spacing: -0.3px; }

  /* Letterhead */
  .letterhead { left: 63px; top: 54px; width: 504px; height: 714px; }
  .letterhead .header-band { position: absolute; left: 0; top: 0; width: 100%; height: 26px; background: var(--blue-deep); }
  .letterhead .header-rule { position: absolute; left: 0; top: 26px; width: 100%; height: 5px; background: var(--orange); }
  .letterhead .side-bar { position: absolute; left: 482px; top: 36px; width: 17px; height: 100px; background: var(--blue); }
  .letterhead .foot-bar { position: absolute; left: 22px; top: 613px; width: 17px; height: 101px; background: var(--orange); }
  .letterhead .brand { right: 30px; top: 72px; }
  .letterhead .brand-dot { width: 16px; height: 16px; }
  .letterhead .brand-name { font-size: 23px; }

  /* Envelope */
  .envelope { left: 613px; top: 94px; width: 550px; height: 244px; }
  .envelope .flap-curve { position: absolute; left: 0; top: 0; }
  .envelope .brand { right: 25px; top: 48px; }
  .envelope .brand-dot { width: 16px; height: 16px; }
  .envelope .brand-name { font-size: 23px; }

  /* Notepad */
  .notepad { left: 702px; top: 368px; width: 295px; height: 428px; }
  .notepad .side-bar { position: absolute; left: 0; top: 0; width: 10px; height: 73px; background: var(--blue); }
  .notepad .foot-bar { position: absolute; right: 0; top: 353px; width: 10px; height: 75px; background: var(--orange); }
  .notepad .brand { left: 15px; top: 36px; gap: 5px; }
  .notepad .brand-dot { width: 12px; height: 12px; }
  .notepad .brand-name { font-size: 17px; }
  .notepad .writing-lines { position: absolute; left: 18px; top: 88px; width: 262px; list-style: none; }
  .notepad .writing-lines li { height: 32px; border-top: 1px solid var(--rule); }
</style>
</head>
<body>

  <section class="sheet letterhead" aria-label="Letterhead">
    <div class="header-band"></div>
    <div class="header-rule"></div>
    <div class="side-bar"></div>
    <div class="brand"><span class="brand-dot"></span><span class="brand-name">Brisk Current</span></div>
    <div class="foot-bar"></div>
  </section>

  <section class="sheet envelope" aria-label="Envelope">
    <svg class="flap-curve" width="90" height="244" viewBox="0 0 90 244" aria-hidden="true">
      <path d="M0 0 H40 Q82 122 38 244 H0 Z" fill="var(--blue)"/>
      <path d="M42 -2 Q86 122 40 246" fill="none" stroke="var(--orange)" stroke-width="5"/>
    </svg>
    <div class="brand"><span class="brand-dot"></span><span class="brand-name">Brisk Current</span></div>
  </section>

  <section class="sheet notepad" aria-label="Notepad">
    <div class="side-bar"></div>
    <div class="brand"><span class="brand-dot"></span><span class="brand-name">Brisk Current</span></div>
    <ul class="writing-lines">
      <li></li><li></li><li></li><li></li><li></li><li></li>
      <li></li><li></li><li></li><li></li><li></li>
    </ul>
    <div class="foot-bar"></div>
  </section>

</body>
</html>
```